Graphic to communicate emotional connection

Howdy-I need a graphic that describe my financial planning process.The attached is a concept, but please use your own creativity to show how you would display this:- The four circles on the outside (Protect what we have, know where it goes, make it grow, and dignity and independence) are the four major areas of concern- Then, there are three value statements:- The first is the most powerful which is that Clarity leads to Control which allows your Intentions to come through- The second shows that we take our clients from Uncertainty and Confusion, to Confidence and Intention- The third says we create space for you to develop your Purposeful Effort which leads to Your Best Financial Life.I've also attached my logo - please use the colors in my logo and maybe add a soft green as needed.The reader should be able to briefly scan this document and understand that we will connect with them on an emotional level to get their finances in shape.Thanks!-Ned

Target Market(s)

wealthy women, whether independent or married

Industry/Entity Type

Financial Planning

Requirements
Must have
• Please use the colors in my logo plus a soft green as needed
Should not have
• This should not be a busy or hard-to-read graphic. It is meant to convey an that I try to make an emotional connection, at a glance.

```html
<!DOCTYPE html>
<html lang="en">
<head>
<meta charset="utf-8">
<title>Financial Planning Process</title>
<link rel="stylesheet" href="https://fonts.googleapis.com/css2?family=Mulish:wght@400;500;600&display=swap">
<style>
  :root {
    --green: #76bd7a;
    --green-soft: #c3efa9;
    --navy: #24488a;
    --navy-dark: #0c3a78;
    --grey: #666666;
    --ink: #5b5b5b;
    --paper: #f9f9f9;
    --bg-edge: #e2e2e2;
  }
  html, body {
    margin: 0;
    padding: 0;
    width: 1200px;
    height: 1200px;
    overflow: hidden;
  }
  body {
    background: radial-gradient(circle at 50% 50%, #ffffff 0%, #f4f4f4 55%, var(--bg-edge) 100%);
    font-family: "Mulish", "Avenir", sans-serif;
  }
  .process-map { display: block; width: 1200px; height: 1200px; }
  .frame-line { stroke: var(--grey); stroke-width: 4; fill: none; }
  .concern-ring { fill: var(--green); }
  .concern-band { fill: none; stroke: var(--grey); stroke-width: 10; }
  .concern-face { fill: var(--paper); }
  .concern-rule { stroke: var(--grey); stroke-width: 2.5; }
  .concern-text { fill: var(--ink); font-size: 23px; text-anchor: middle; font-weight: 400; }
  .concern-text.small { font-size: 19px; }
  .step-halo { fill: var(--green-soft); stroke: var(--green); stroke-width: 2; }
  .step-ring { fill: var(--paper); stroke: var(--navy); stroke-width: 10; }
  .step-accent { fill: none; stroke: var(--green); stroke-width: 7; }
  .connector { stroke: var(--green); stroke-width: 1.5; }
  .next-badge { fill: var(--navy-dark); }
  .next-chevron { fill: none; stroke: #ffffff; stroke-width: 4; stroke-linecap: round; stroke-linejoin: round; }
  .value-title { fill: var(--ink); font-size: 25px; font-weight: 500; text-anchor: middle; letter-spacing: 0.5px; }
  .value-label { fill: var(--ink); font-size: 17px; font-weight: 500; text-anchor: middle; letter-spacing: 0.6px; }
  .lead-text { fill: var(--ink); font-size: 12px; font-weight: 500; text-anchor: middle; letter-spacing: 0.4px; }
  .arc-text { fill: var(--ink); font-size: 15px; font-weight: 500; letter-spacing: 0.6px; }
  .icon-stroke { fill: none; stroke: var(--grey); stroke-linecap: round; }
  .icon-fill { fill: var(--grey); }
  .gear-hole { fill: var(--paper); }
  .figure-placeholder { fill: #d9d9d9; }
</style>
</head>
<body>
<svg class="process-map" viewBox="0 0 1200 1200" xmlns="http://www.w3.org/2000/svg">
  <defs>
    <path id="arc-take" d="M378,643 A86,86 0 0 1 500,553"/>
    <path id="arc-space" d="M388,914 A86,86 0 1 1 525,810"/>
  </defs>

  <g class="frame">
    <line class="frame-line" x1="200" y1="213" x2="1000" y2="213"/>
    <line class="frame-line" x1="200" y1="1007" x2="1000" y2="1007"/>
    <line class="frame-line" x1="200" y1="213" x2="200" y2="987"/>
    <line class="frame-line" x1="1000" y1="213" x2="1000" y2="987"/>
  </g>

  <g class="concern concern-protect">
    <circle class="concern-ring" cx="200" cy="213" r="108"/>
    <circle class="concern-band" cx="200" cy="213" r="86"/>
    <circle class="concern-face" cx="200" cy="213" r="81"/>
    <line class="concern-rule" x1="170" y1="161" x2="230" y2="161"/>
    <text class="concern-text" x="200" y="190">PROTECT</text>
    <text class="concern-text" x="200" y="218">WHAT</text>
    <text class="concern-text" x="200" y="245">WE HAVE</text>
    <line class="concern-rule" x1="170" y1="259" x2="230" y2="259"/>
  </g>
  <g class="concern concern-know">
    <circle class="concern-ring" cx="1000" cy="213" r="108"/>
    <circle class="concern-band" cx="1000" cy="213" r="86"/>
    <circle class="concern-face" cx="1000" cy="213" r="81"/>
    <line class="concern-rule" x1="970" y1="161" x2="1030" y2="161"/>
    <text class="concern-text" x="1000" y="191">KNOW</text>
    <text class="concern-text" x="1000" y="218">WHERE</text>
    <text class="concern-text" x="1000" y="245">IT GOES</text>
    <line class="concern-rule" x1="970" y1="259" x2="1030" y2="259"/>
  </g>
  <g class="concern concern-grow">
    <circle class="concern-ring" cx="200" cy="987" r="108"/>
    <circle class="concern-band" cx="200" cy="987" r="86"/>
    <circle class="concern-face" cx="200" cy="987" r="81"/>
    <line class="concern-rule" x1="170" y1="943" x2="230" y2="943"/>
    <text class="concern-text" x="200" y="978">MAKE</text>
    <text class="concern-text" x="200" y="1005">IT GROW</text>
    <line class="concern-rule" x1="170" y1="1023" x2="230" y2="1023"/>
  </g>
  <g class="concern concern-dignity">
    <circle class="concern-ring" cx="1000" cy="987" r="108"/>
    <circle class="concern-band" cx="1000" cy="987" r="86"/>
    <circle class="concern-face" cx="1000" cy="987" r="81"/>
    <line class="concern-rule" x1="970" y1="943" x2="1030" y2="943"/>
    <text class="concern-text" x="1000" y="972">DIGNITY</text>
    <text class="concern-text" x="1000" y="991">AND</text>
    <text class="concern-text small" x="1000" y="1011">INDEPENDENCE</text>
    <line class="concern-rule" x1="970" y1="1023" x2="1030" y2="1023"/>
  </g>

  <g class="value-row value-clarity">
    <line class="connector" x1="405" y1="385" x2="525" y2="385"/>
    <line class="connector" x1="675" y1="385" x2="796" y2="385"/>

    <g class="step step-clarity">
      <path class="step-accent" d="M250,385 A80,80 0 0 1 330,305"/>
      <circle class="step-halo" cx="330" cy="385" r="75"/>
      <circle class="step-ring" cx="330" cy="385" r="57"/>
      <circle class="icon-stroke" cx="325" cy="379" r="18" stroke-width="6"/>
      <line class="icon-stroke" x1="339" y1="394" x2="352" y2="407" stroke-width="8"/>
    </g>
    <g class="next-badge-group">
      <circle class="next-badge" cx="463" cy="385" r="19"/>
      <path class="next-chevron" d="M459,376 L468,385 L459,394"/>
    </g>
    <g class="step step-control">
      <path class="step-accent" d="M543,442 A80,80 0 0 0 657,442"/>
      <circle class="step-halo" cx="600" cy="385" r="75"/>
      <circle class="step-ring" cx="600" cy="385" r="57"/>
      <g class="gear gear-large" transform="translate(587,371)">
        <rect class="icon-fill" x="-4.5" y="-23" width="9" height="46" rx="1.5"/>
        <rect class="icon-fill" x="-4.5" y="-23" width="9" height="46" rx="1.5" transform="rotate(45)"/>
        <rect class="icon-fill" x="-4.5" y="-23" width="9" height="46" rx="1.5" transform="rotate(90)"/>
        <rect class="icon-fill" x="-4.5" y="-23" width="9" height="46" rx="1.5" transform="rotate(135)"/>
        <circle class="icon-fill" r="17"/>
        <circle class="gear-hole" r="7"/>
      </g>
      <g class="gear gear-small" transform="translate(618,402)">
        <rect class="icon-fill" x="-3.5" y="-17" width="7" height="34" rx="1.2" transform="rotate(22.5)"/>
        <rect class="icon-fill" x="-3.5" y="-17" width="7" height="34" rx="1.2" transform="rotate(67.5)"/>
        <rect class="icon-fill" x="-3.5" y="-17" width="7" height="34" rx="1.2" transform="rotate(112.5)"/>
        <rect class="icon-fill" x="-3.5" y="-17" width="7" height="34" rx="1.2" transform="rotate(157.5)"/>
        <circle class="icon-fill" r="12.5"/>
        <circle class="gear-hole" r="5"/>
      </g>
    </g>
    <g class="next-badge-group">
      <circle class="next-badge" cx="737" cy="385" r="19"/>
      <path class="next-chevron" d="M733,376 L742,385 L733,394"/>
    </g>
    <g class="step step-intention">
      <path class="step-accent" d="M871,305 A80,80 0 0 1 946,358"/>
      <circle class="step-halo" cx="871" cy="385" r="75"/>
      <circle class="step-ring" cx="871" cy="385" r="57"/>
      <circle class="icon-stroke" cx="871" cy="385" r="31" stroke-width="4"/>
      <circle class="icon-stroke" cx="871" cy="385" r="22" stroke-width="4"/>
      <circle class="icon-stroke" cx="871" cy="385" r="13" stroke-width="4"/>
      <circle class="icon-fill" cx="871" cy="385" r="4"/>
      <line class="icon-stroke" x1="871" y1="385" x2="900" y2="356" stroke-width="3"/>
      <path class="icon-fill" d="M898,350 L906,350 L906,358 L900,364 L892,356 Z"/>
    </g>

    <text class="value-title" x="330" y="497">CLARITY</text>
    <text class="value-title" x="600" y="497">CONTROL</text>
    <text class="value-title" x="871" y="497">INTENTION</text>
  </g>

  <g class="value-row value-confidence">
    <text class="arc-text"><textPath href="#arc-take">WE TAKE YOU FROM</textPath></text>
    <line class="connector" x1="530" y1="630" x2="680" y2="630"/>
    <g class="step step-uncertainty">
      <path class="step-accent" d="M393,642 A71,71 0 0 1 463,559"/>
      <circle class="step-halo" cx="463" cy="630" r="67"/>
      <circle class="step-ring" cx="463" cy="630" r="51"/>
      <circle class="figure-placeholder" cx="463" cy="630" r="30" role="img" aria-label="Uncertain person scratching head at a crossroads"/>
    </g>
    <text class="lead-text" x="605" y="608">WHICH LEADS TO</text>
    <g class="next-badge-group">
      <circle class="next-badge" cx="605" cy="630" r="17"/>
      <path class="next-chevron" d="M601,622 L609,630 L601,638"/>
    </g>
    <g class="step step-confidence">
      <path class="step-accent" d="M747,559 A71,71 0 0 1 818,636"/>
      <circle class="step-halo" cx="747" cy="630" r="67"/>
      <circle class="step-ring" cx="747" cy="630" r="51"/>
      <circle class="figure-placeholder" cx="747" cy="630" r="30" role="img" aria-label="Confident person standing with arms crossed"/>
    </g>
    <text class="value-label" x="463" y="721">UNCERTANITY CONFUSION</text>
    <text class="value-label" x="747" y="721">CONFIDENCE INTENTION</text>
  </g>

  <g class="value-row value-effort">
    <text class="arc-text"><textPath href="#arc-space">WE CREATE SPACE FOR YOUR</textPath></text>
    <line class="connector" x1="530" y1="870" x2="680" y2="870"/>
    <g class="step step-effort">
      <path class="step-accent" d="M393,882 A71,71 0 0 1 463,799"/>
      <circle class="step-halo" cx="463" cy="870" r="67"/>
      <circle class="step-ring" cx="463" cy="870" r="51"/>
      <circle class="figure-placeholder" cx="463" cy="870" r="30" role="img" aria-label="Person pushing a large gear"/>
    </g>
    <text class="lead-text" x="605" y="848">WHICH LEADS TO</text>
    <g class="next-badge-group">
      <circle class="next-badge" cx="605" cy="870" r="17"/>
      <path class="next-chevron" d="M601,862 L609,870 L601,878"/>
    </g>
    <g class="step step-best-life">
      <path class="step-accent" d="M747,799 A71,71 0 0 1 818,876"/>
      <circle class="step-halo" cx="747" cy="870" r="67"/>
      <circle class="step-ring" cx="747" cy="870" r="51"/>
      <circle class="figure-placeholder" cx="747" cy="870" r="30" role="img" aria-label="Potted plant growing a dollar-sign leaf"/>
    </g>
    <text class="value-label" x="463" y="963">PURPOSEFUL EFFORT</text>
    <text class="value-label" x="747" y="963">YOUR BEST FINANCIAL LIFE</text>
  </g>
</svg>
</body>
</html>
```